Residential Construction Business - Site Signage

I need a design made for a site fence banner. We have a logo and branding so the design would need to be aligned with this. It would need to be made to specific size ratio so that it can be sent to the maker for production.
ratio : 4600 wide x 1700 high
The design should feature our website and also the slogan
"don't move, re-imagine"

Target Market(s)

potential clients

Industry/Entity Type

construction

Font styles to use
Other font styles liked:
• to match branding

Colors
0054AA
0677BA
7BADD7
CADEEF
E8F1F8

Requirements
Must have
• www.velmbuild.com.au Majority of the sign is our brand logo
Nice to have
• Majority of the sign is our brand logo
Should not have
• colors and themes that arent brand relevant

```html
<!DOCTYPE html>
<html lang="en">
<head>
<meta charset="utf-8">
<title>Velm Build – Site Fence Banner</title>
<link rel="stylesheet" href="https://fonts.googleapis.com/css2?family=Montserrat:wght@400;500;700&display=swap">
<style>
  :root {
    --backdrop: #9b9b9b;
    --navy: #244a67;
    --paper: #ffffff;
    --paper-shade: #f3f3f3;
  }
  * { margin: 0; padding: 0; box-sizing: border-box; }
  html, body {
    width: 1200px;
    height: 1155px;
    overflow: hidden;
    background: var(--backdrop);
    font-family: "Montserrat", sans-serif;
  }
  .banner {
    position: absolute;
    left: 179px;
    top: 407px;
    width: 842px;
    height: 340px;
    overflow: hidden;
  }
  .banner-shapes {
    position: absolute;
    inset: 0;
    width: 842px;
    height: 340px;
  }
  .brand-name {
    position: absolute;
    left: 43px;
    top: 154px;
    display: flex;
    align-items: center;
    gap: 12px;
    color: var(--navy);
    font-weight: 700;
    font-size: 26px;
    letter-spacing: 0.22em;
    line-height: 1;
  }
  .brand-square {
    width: 26px;
    height: 26px;
    background: var(--navy);
    flex: none;
  }
  .slogan {
    position: absolute;
    left: 358px;
    top: 146px;
    color: var(--paper);
    font-size: 36px;
    line-height: 1;
    letter-spacing: -0.01em;
    white-space: nowrap;
  }
  .slogan strong { font-weight: 700; }
  .slogan span { font-weight: 400; }
  .website {
    position: absolute;
    left: 43px;
    top: 295px;
    color: var(--navy);
    font-weight: 500;
    font-size: 17px;
    line-height: 1;
    letter-spacing: 0.01em;
  }
</style>
</head>
<body>
  <section class="banner">
    <svg class="banner-shapes" viewBox="0 0 842 340" aria-hidden="true">
      <defs>
        <linearGradient id="paperFade" x1="0" y1="0" x2="1" y2="0">
          <stop offset="0" stop-color="var(--paper)"/>
          <stop offset="1" stop-color="var(--paper-shade)"/>
        </linearGradient>
      </defs>
      <rect class="field-light" x="0" y="0" width="842" height="340" fill="url(#paperFade)"/>
      <path class="chevron-white" d="M374 0 H842 V340 H384 L240 182 Q234 170 240 158 Z" fill="var(--paper)"/>
      <path class="chevron-navy" d="M467 0 H842 V340 H479 L332 182 Q326 170 332 158 Z" fill="var(--navy)"/>
      <path class="url-tab" d="M0 293 H43 L32 306.5 L43 320 H0 Z" fill="var(--navy)"/>
    </svg>

    <div class="brand-name"><i class="brand-square"></i>VELM BUILD</div>

    <p class="slogan"><strong>don't move,</strong> <span>re-imagine</span></p>

    <p class="website">www.velmbuild.com.au</p>
  </section>
</body>
</html>
```